Web Design Project for a new website

We need a web design for a new proposed social media site ,intially to judge market response, this would be a basic site 4 pages with a register page for visitors to register with email and possibly start their own profile page with a template that would be on the site.
the domain is plokkit.net with the tagline rise onward stand truly plokkit ,,it has 2 aa in plokkit ,the main function and the message we would like to convey is that if you aspire to achieve your goals,aim in life ,change your life ,the site will recognize and reward you with a status rank more like a life rank,example is halvane 1000 most influential people,this would allow you to network with other likeminded people who register on site and progress of your goal could be monitored via your profile page.
There are 4 categories of how to become world plokkit
Star,Hero,Leader,Icon
And one category Q-7 which is a open forum on the science of success to which people registered can contribute and source info.
The design has to communicate the message of the site in a proffessional modern way with distinct colours and and logo that can be visually striking .

deadline is friday the 5th please submit your designs

Please submit designs as last day of deadline 5th august.

Reason: some designers have asked for extra time so obliging but cant extend any further so please submit designs by deadline .

Reason: 1 designer has asked for days extension.

12 to 80 all levels

Media

• see attached file for logo and design of plokkit the file can be changed or formatted or if be your own individual design on the same theme ,the main web logo of plokkit would also be the logo with a different colour identity fo categories STAR,HERO,LEADER,ICON ,Q-7
• plokkit.net should have the tagline rise,onward,stand truly plokkit
plokkit.net
rise,onward,stand truly plokkit,
the logo should indicate being world plokkit,a globe as per file image.some background messages like aspire,achive,be a world leader,can be used as background.

```html
<!DOCTYPE html>
<html lang="en">
<head>
<meta charset="utf-8">
<title>plokkit.net</title>
<link rel="stylesheet" href="https://fonts.googleapis.com/css2?family=Arimo:wght@400;700&display=swap">
<style>
:root{
  --bg-top:#bccdd5;
  --bg-bottom:#e4edf0;
  --purple:#8a5a9e;
  --ink:#3c4a55;
  --nav-top:#a9c0d0;
  --nav-bottom:#5f8199;
  --band:#d9d3c0;
  --red:#ee2e24;
  --card:#c6cad1;
  --star:#f28c0f;
  --hero:#2f6fad;
  --leader:#5a9a22;
  --icon:#c0296f;
  --link:#4a6070;
  --rule:#7fb3b8;
}
*{box-sizing:border-box;margin:0;padding:0}
html,body{width:1200px;height:780px;overflow:hidden}
body{
  position:relative;
  font-family:"Arimo",Arial,sans-serif;
  background:linear-gradient(180deg,var(--bg-top) 0%,#d4e1e6 40%,var(--bg-bottom) 100%);
  color:var(--ink);
}
.abs{position:absolute}

/* header */
.brand-box{left:120px;top:43px;width:307px;height:80px;border-radius:8px;
  background:linear-gradient(180deg,#f4f4f8,#e3e3ec);box-shadow:0 2px 8px rgba(60,80,100,.35);}
.brand-dot{left:16px;top:14px;width:56px;height:56px;border-radius:50%;background:var(--purple)}
.brand-name{left:84px;top:14px;font-size:30px;font-weight:400;color:var(--purple);letter-spacing:.5px}
.brand-tagline{left:86px;top:50px;font-size:11.5px;color:var(--purple)}

.login-label{left:449px;top:72px;font-size:12.5px;color:var(--ink)}
.field{top:64px;height:28px;border:1px solid #c7c2a8;border-radius:4px;
  background:linear-gradient(180deg,#fbfaf3,#e6e2cc);font-size:11px;color:#9a9f9f;padding:8px 14px}
.field.user{left:485px;width:170px}
.field.pass{left:664px;width:170px}
.join{left:846px;top:64px;width:70px;height:28px;border-radius:4px;border:1px solid #b3b3bb;
  background:linear-gradient(180deg,#e8e8ee,#c7c7d0);font-size:12px;color:#4a4f5a;text-align:center;line-height:26px}
.forgot{left:564px;top:104px;font-size:11px;color:var(--link)}
.remember{left:674px;top:104px;font-size:11px;color:var(--link)}
.remember i{display:inline-block;width:10px;height:10px;border:1px solid #999;background:#fff;margin-right:7px;vertical-align:-1px}
.promo{left:936px;top:63px;font-size:13.5px;line-height:16px;color:var(--purple)}

/* navigation */
.nav-band{left:107px;top:150px;width:986px;height:38px}
.nav{left:137px;top:150px;width:930px;height:38px;
  background:linear-gradient(180deg,var(--nav-top),#7f9db1 55%,var(--nav-bottom));}
.nav-item{top:150px;height:38px;line-height:40px;font-size:14px;color:#f2f6f8;text-align:center}
.nav-item.active{background:rgba(40,70,95,.3)}
.nav-sep{top:158px;width:1px;height:22px;background:rgba(255,255,255,.35)}
.advanced{left:763px;top:157px;width:76px;height:27px;border-radius:4px 0 0 4px;
  background:linear-gradient(180deg,#e6f0ef,#b9d2d4);font-size:12.5px;color:#3a5f6e;line-height:27px;padding-left:6px}
.search{left:838px;top:157px;width:215px;height:27px;border-radius:0 4px 4px 0;
  background:linear-gradient(180deg,#fbfaf4,#e6e2cf);font-size:12.5px;color:#4a5560;line-height:27px;padding-left:18px}

/* feature panel */
.feature{left:137px;top:225px;width:930px;height:200px;border-radius:6px;background:var(--red);
  box-shadow:0 10px 8px -6px rgba(40,40,40,.5)}
.feature-badge{left:180px;top:200px;width:66px;height:66px;border-radius:50%;
  background:radial-gradient(circle at 45% 40%,#f26a2a,#d8380e);border:3px solid #fff;box-shadow:0 2px 4px rgba(0,0,0,.3)}
.feature-title{left:158px;top:274px;font-size:16px;font-weight:700;color:#fff}
.feature-text{font-size:12px;line-height:14.6px;color:#fff}
.feature-text.left{left:156px;top:296px;width:440px}
.feature-text.right{left:616px;top:284px;width:440px}

/* categories */
.cat-row{left:150px;top:465px;width:905px;height:140px}
.cat-badge{top:452px;width:66px;height:66px;border-radius:50%;border:3px solid #fff;box-shadow:0 2px 4px rgba(0,0,0,.3)}
.cat-badge.star{left:177px;background:radial-gradient(circle,#f6c324,#e7930c)}
.cat-badge.hero{left:418px;background:radial-gradient(circle,#3c8bd0,#1f5b98)}
.cat-badge.leader{left:631px;background:radial-gradient(circle,#6ab12e,#3c7a18)}
.cat-badge.icon{left:844px;background:radial-gradient(circle,#d24f8d,#a41c5d)}
.cat-title{top:482px;font-size:20px;font-weight:700}
.cat-title.star{left:253px;color:var(--star)}
.cat-title.hero{left:496px;color:var(--hero)}
.cat-title.leader{left:705px;color:var(--leader)}
.cat-title.icon{left:923px;color:var(--icon)}
.cat-text{top:525px;width:190px;font-size:12.5px;line-height:14.6px;color:#4a4f57}
.cat-text a{color:#4a4f57;font-weight:700;font-size:11px;text-decoration:underline;margin-left:6px}

/* footer */
.rule{left:137px;width:943px;height:1px;background:linear-gradient(90deg,transparent,var(--rule) 20%,var(--rule) 80%,transparent)}
.social{width:26px;height:26px;border-radius:50%;background:#4a6a94}
.footer-links{left:879px;top:653px;font-size:11px;line-height:14px;color:var(--link);list-style:none}
.copyright{left:858px;top:738px;font-size:10px;color:var(--link)}
</style>
</head>
<body>

<header>
  <div class="abs brand-box">
    <span class="abs brand-dot"></span>
    <span class="abs brand-name">plokkit.net</span>
    <span class="abs brand-tagline">rise, onward, stand truly plokkit</span>
  </div>

  <span class="abs login-label">Login</span>
  <div class="abs field user">Username</div>
  <div class="abs field pass">Password</div>
  <div class="abs join">Join</div>
  <span class="abs forgot">Forget password</span>
  <span class="abs remember"><i></i>Remember</span>
  <p class="abs promo">World's largest website<br>for plokkit people</p>
</header>

<nav>
  <svg class="abs nav-band" width="986" height="38" viewBox="0 0 986 38">
    <polygon points="0,8 30,0 30,38 0,34 12,20" fill="#8aa5b5"/>
    <polygon points="986,8 956,0 956,38 986,34 974,20" fill="#8aa5b5"/>
    <rect x="30" y="22" width="926" height="16" fill="#d9d3c0"/>
  </svg>
  <div class="abs nav"></div>
  <svg class="abs" style="left:160px;top:159px" width="26" height="22" viewBox="0 0 26 22">
    <polygon points="13,1 25,11 21,11 21,21 16,21 16,14 10,14 10,21 5,21 5,11 1,11" fill="#f2f6f8"/>
  </svg>
  <span class="abs nav-sep" style="left:208px"></span>
  <span class="abs nav-item" style="left:222px;width:90px">About Us</span>
  <span class="abs nav-sep" style="left:322px"></span>
  <span class="abs nav-item" style="left:334px;width:92px">My Profile</span>
  <span class="abs nav-item active" style="left:436px;width:69px">Q-7</span>
  <span class="abs nav-item" style="left:510px;width:94px">Register</span>
  <span class="abs nav-sep" style="left:609px"></span>
  <span class="abs nav-item" style="left:618px;width:100px">Contact Us</span>
  <span class="abs nav-sep" style="left:725px"></span>
  <div class="abs advanced">Advanced <svg width="9" height="6" viewBox="0 0 9 6"><polygon points="0,0 9,0 4.5,6" fill="#3a5f6e"/></svg></div>
  <div class="abs search">Search</div>
  <svg class="abs" style="left:1022px;top:162px" width="18" height="18" viewBox="0 0 18 18">
    <circle cx="7" cy="7" r="5" fill="none" stroke="#7a8088" stroke-width="2"/>
    <line x1="11" y1="11" x2="16" y2="16" stroke="#7a8088" stroke-width="2.5"/>
  </svg>
</nav>

<main>
  <section>
    <div class="abs feature"></div>
    <div class="abs feature-badge" role="img" aria-label="Q-7 category emblem"></div>
    <h1 class="abs feature-title">Q-7: The Science of Winning</h1>
    <p class="abs feature-text left">Lorem ipsum dolor sit amet, consectetur adipiscing elit. Sed tempor, felis id rhoncus tempor, ipsum nisi tincidunt massa, vitae euismod ante est in libero. Curabitur enim quam, placerat volutpat ultricies eget, molestie sed mi. Donec ut diam vel ligula hendrerit vehicula a a augue. Nam sed eros elit. Mauris dolor nibh, imperdiet id posuere at, suscipit aliquet ipsum. Nunc dignissim cursus facilisis. Sed venenatis cursus est in laoreet. Cum sociis natoque penatibus et magnis dis parturient montes, nascetur ridiculus mus.</p>
    <p class="abs feature-text right">In hac habitasse platea dictumst. Aliquam lobortis pretium purus, vel placerat mauris pretium sit amet.<br>Duis sed vehicula tellus. Donec turpis massa, porttitor sit amet vulputate a, consectetur eu sapien<br><br>In consequat, tortor eu lacinia pharetra, mi purus imperdiet eros, ac feugiat risus ipsum tempus dolor. Donec nec est magna. Nulla suscipit porttitor odio. Maece-nas mauris libero, aliquet sit amet tempus eu, aliquet ut odio.</p>
  </section>

  <section>
    <svg class="abs cat-row" width="905" height="140" viewBox="0 0 905 140">
      <path d="M15,7 H232 L270,68 L232,130 H15 Q7,130 7,122 V15 Q7,7 15,7 Z" fill="#c6cad1"/>
      <path d="M244,7 H444 L481,68 L444,130 H244 L270,90 Q283,68 270,46 Z" fill="#c6cad1"/>
      <path d="M455,7 H655 L692,68 L655,130 H455 L481,90 Q494,68 481,46 Z" fill="#c6cad1"/>
      <path d="M666,7 H888 Q896,7 896,15 V122 Q896,130 888,130 H666 L692,90 Q705,68 692,46 Z" fill="#c6cad1"/>
    </svg>

    <div class="abs cat-badge star" role="img" aria-label="Star category emblem"></div>
    <h2 class="abs cat-title star">STAR</h2>
    <p class="abs cat-text" style="left:183px">Lorem ipsum dolor sit amet, con-sectetur adipisicing elit, sed do eiusmod tempor incididunt ut labore et dolore magna...<a>more</a></p>

    <div class="abs cat-badge hero" role="img" aria-label="Hero category emblem"></div>
    <h2 class="abs cat-title hero">HERO</h2>
    <p class="abs cat-text" style="left:438px">Lorem ipsum dolor sit amet, con-sectetur adipisicing elit, sed do eiusmod tempor incididunt ut labore et dolore...<a>more</a></p>

    <div class="abs cat-badge leader" role="img" aria-label="Leader category emblem"></div>
    <h2 class="abs cat-title leader">LEADER</h2>
    <p class="abs cat-text" style="left:650px">Lorem ipsum dolor sit amet, con-sectetur adipisicing elit, sed do eiusmod tempor incididunt ut labore et dolore...<a>more</a></p>

    <div class="abs cat-badge icon" role="img" aria-label="Icon category emblem"></div>
    <h2 class="abs cat-title icon">ICON</h2>
    <p class="abs cat-text" style="left:862px">Lorem ipsum dolor sit amet, con-sectetur adipisicing elit, sed do eiusmod tempor incididunt ut labore et dolore...<a>more</a></p>
  </section>
</main>

<footer>
  <span class="abs rule" style="top:632px"></span>
  <span class="abs social" style="left:787px;top:650px;background:#e0701a"></span>
  <span class="abs social" style="left:823px;top:650px;background:#3a8cc4"></span>
  <span class="abs social" style="left:787px;top:684px;background:#34508a"></span>
  <span class="abs social" style="left:823px;top:684px;background:#3a7eb0"></span>
  <ul class="abs footer-links">
    <li>Media</li>
    <li>Developers</li>
    <li>Terms &amp; Conditions</li>
    <li>Privacy Policy</li>
  </ul>
  <span class="abs rule" style="top:725px"></span>
  <span class="abs copyright">© 2011 plokkit.net</span>
</footer>

</body>
</html>
```